We need a logo and landing page designed. We are a full-service general contractor based in Tempe Arizona. We can provide all phases of construction from design to completion. We specialize in commercial and residential remodels, as well as ground-up construction. We will like to see designs that primarily used reds, blues, blacks, whites, etc. The design should be a professional yet fun, easy-to-read format. Our name is Oak Harbor Construction...I would like to see some designs that incorporate a "oak harbor" and some without.
The final design should communicate a professional, quality-driven, safety oriented full service business.

Target Market(s)

Building owners, land developers, homeowners

Industry/Entity Type

Commercial Construction

Coding

Coded - Design and coding required

Number of Pages Required

1 page

Font styles to use
Serif

Colors
0054AA
0677BA
7BADD7
CADEEF
E8F1F8
59FF00
82FF00
B8FF75
E3FFCB
F4FFEA
EE7325
F08F49
F5BC92
FAE3D3
FDF4ED
EB3D1F
EC4F4E
F09395
F8D3D4
FCEDEE

```html
<!DOCTYPE html>
<html lang="en">
<head>
<meta charset="utf-8">
<title>Oak Harbor Construction</title>
<link href="https://fonts.googleapis.com/css2?family=Lexend:wght@400;600;700;800&family=Open+Sans:ital,wght@0,400;0,600;1,400&display=swap" rel="stylesheet">
<style>
:root{
  --red:#EB3D1F;
  --orange:#EE7325;
  --ink:#111111;
  --body:#555555;
  --line:#d8d8d8;
  --white:#ffffff;
  --foot:#0c0c0c;
}
*{box-sizing:border-box;margin:0;padding:0}
html,body{width:1200px;height:4246px;overflow:hidden;background:var(--white)}
body{position:relative;font-family:"Open Sans",sans-serif;color:var(--body)}
.abs{position:absolute}
.head{font-family:"Lexend",sans-serif;font-weight:700;color:var(--ink);text-transform:uppercase;letter-spacing:-.5px}
.head .accent{color:var(--red)}
.btn{position:absolute;display:flex;align-items:center;justify-content:center;gap:14px;font-family:"Lexend",sans-serif;font-weight:600;font-size:15px;text-transform:uppercase;border:2px solid var(--red);color:var(--red);background:var(--white)}
.btn.solid{background:var(--red);color:var(--white)}
.btn svg{width:30px;height:10px}
.photo{position:absolute}
/* header */
.logo-box{left:0;top:0;width:315px;height:71px;background:var(--white);display:flex;align-items:center;padding-left:58px;gap:10px;z-index:3}
.logo-mark{width:22px;height:22px;background:var(--red)}
.logo-name{font-family:"Lexend",sans-serif;font-weight:700;font-size:17px;line-height:1.05;color:var(--ink);text-transform:uppercase}
.nav{left:628px;top:28px;display:flex;gap:0;font-size:12px;color:#222;text-transform:uppercase;z-index:3}
.nav span{position:absolute;white-space:nowrap}
.phone-btn{left:982px;top:18px;width:158px;height:38px;border:2px solid var(--red);color:var(--red);font-family:"Lexend",sans-serif;font-weight:600;font-size:17px;display:flex;align-items:center;justify-content:center;gap:8px;z-index:3}
/* hero */
.hero-title{left:58px;top:270px;font-family:"Lexend",sans-serif;font-weight:800;font-size:57px;line-height:66px;color:var(--white);text-transform:uppercase;letter-spacing:1px}
.hero-title .accent{color:var(--orange)}
.hero-sub{left:62px;top:410px;font-style:italic;font-size:15.5px;line-height:25px;color:var(--white)}
/* about */
.about-kicker{left:143px;top:785px;font-size:16px;color:#222}
.about-title{left:143px;top:812px;font-size:32px;line-height:37px}
.about-tag{left:143px;top:895px;font-style:italic;font-size:13px;line-height:21px;color:var(--red)}
.about-text{left:143px;top:952px;width:390px;font-size:12px;line-height:21px}
.about-text p+p{margin-top:14px}
/* sections */
.kicker{width:1200px;left:0;text-align:center;font-size:15px;color:#222}
.sec-title{width:1200px;left:0;text-align:center;font-size:33px}
.card{position:absolute;top:1341px;width:270px;height:338px;border:2px solid #6d6d6d;text-align:center}
.card.active{border-color:var(--red)}
.card svg.icon{position:absolute;left:100px;top:30px;width:70px;height:76px}
.card h3{position:absolute;top:130px;left:0;width:100%;font-family:"Lexend",sans-serif;font-weight:600;font-size:17px;line-height:25px;color:var(--ink);text-transform:uppercase}
.card p{position:absolute;top:196px;left:22px;width:222px;font-size:12px;line-height:19px}
.card .btn{left:45px;top:274px;width:173px;height:40px}
/* news */
.news{position:absolute;top:2783px;width:290px;height:420px}
.news .frame{position:absolute;left:254px;top:-14px;width:44px;height:200px;border:2px solid var(--orange);border-left:none}
.news .date{position:absolute;left:-28px;top:221px;width:140px;height:30px;background:var(--red);color:var(--white);font-size:12px;font-weight:600;display:flex;align-items:center;justify-content:center}
.news h4{position:absolute;top:276px;left:0;font-family:"Lexend",sans-serif;font-weight:600;font-size:13.5px;color:var(--ink);text-transform:uppercase}
.news p{position:absolute;top:303px;left:0;width:250px;font-size:11.5px;line-height:19px}
.news .more{position:absolute;top:375px;left:250px;font-size:14px;color:var(--red);text-decoration:underline}
/* contact */
.contact-card{left:282px;top:3307px;width:636px;height:511px;background:var(--white);box-shadow:0 2px 18px rgba(0,0,0,.08)}
.field{position:absolute;border:1px solid #bdbdbd;font-size:10.5px;color:#666;padding:10px 14px}
/* footer */
.footer{left:0;top:3926px;width:1200px;height:320px;background:var(--foot);color:#d0d0d0}
.footer .fh{position:absolute;font-family:"Lexend",sans-serif;font-weight:700;font-size:19px;color:var(--white);text-transform:uppercase}
.footer .fh .accent{color:var(--red)}
.footer .small{font-size:11.5px;line-height:18px}
.social{position:absolute;top:4110px;width:40px;height:40px;border:1.5px solid var(--red);border-radius:50%}
.sitemap li{list-style:none;position:absolute;left:0;font-size:11.5px;padding-left:16px}
.sitemap li::before{content:"";position:absolute;left:0;top:5px;width:6px;height:6px;border:1.5px solid var(--red);border-radius:50%}
</style>
</head>
<body>

<!-- HERO -->
<div class="photo" style="left:0;top:0;width:633px;height:712px;background:linear-gradient(135deg,#3b352d 0%,#6b5f4d 45%,#2c2a26 100%)" role="img" aria-label="Unfinished room with bare walls, ladder and debris before renovation"></div>
<div class="photo" style="left:633px;top:0;width:567px;height:712px;background:linear-gradient(180deg,#e9e9e7 0%,#d9d7d2 55%,#b07a45 75%,#8c5a2c 100%)" role="img" aria-label="Bright renovated room with white walls, tall window and parquet floor"></div>
<div class="photo" style="left:1078px;top:305px;width:122px;height:132px;border:3px solid var(--red);background:linear-gradient(180deg,#9fb6cc 0%,#c9cfd2 55%,#8a6a4a 100%)" role="img" aria-label="Building frame under construction on a site"></div>

<div class="abs logo-box"><span class="logo-mark"></span><span class="logo-name">Oak Harbor<br>Construction</span></div>
<div class="abs nav">
  <svg class="abs" style="left:0;top:10px" width="12" height="12" viewBox="0 0 12 12"><path d="M0 12 L12 0 L12 12Z" fill="var(--orange)"/></svg>
  <span style="left:12px;color:var(--orange)">Home</span>
  <span style="left:64px">Services</span>
  <span style="left:137px">Projects</span>
  <span style="left:211px">News</span>
  <span style="left:264px">Contact Us</span>
</div>
<div class="abs phone-btn">
  <svg width="18" height="18" viewBox="0 0 24 24" fill="none" stroke="currentColor" stroke-width="2"><path d="M5 3h4l2 5-3 2a11 11 0 0 0 6 6l2-3 5 2v4a2 2 0 0 1-2 2A17 17 0 0 1 3 5a2 2 0 0 1 2-2z"/></svg>
  480.555.0142
</div>

<div class="abs hero-title">Commercial<br><span class="accent">Remodeling</span></div>
<div class="abs hero-sub">We Specialize In Commercial And Residential Remodels,<br>As Well As Ground-Up Construction</div>
<div class="btn solid" style="left:59px;top:478px;width:173px;height:41px">Contact Us <svg viewBox="0 0 30 10"><path d="M0 5h27M23 1l4 4-4 4" stroke="currentColor" stroke-width="1.5" fill="none"/></svg></div>

<!-- ABOUT -->
<svg class="abs" style="left:0;top:712px" width="1200" height="290"><defs><linearGradient id="tri" x1="0" y1="0" x2="1" y2="1"><stop offset="0" stop-color="#EB3D1F"/><stop offset="1" stop-color="#EE7325"/></linearGradient></defs><path d="M906 0H1200V285Z" fill="url(#tri)"/></svg>
<div class="abs about-kicker">About</div>
<div class="abs about-title head"><span class="accent">Oak Harbor</span><br>Construction</div>
<div class="abs about-tag">We Specialize In Commercial And Residential Remodels, As<br>Well As Ground-Up Construction</div>
<div class="abs about-text">
  <p>Lorem Ipsum has been the industry's standard dummy text ever since the 1500s, when an unknown printer took a galley of type and scrambled it to make a type specimen book. It has survived not only five centuries, but also the leap into electronic.</p>
  <p>Lorem Ipsum has been the industry's standard dummy text ever since the &nbsp;when an unknown printer took a galley.</p>
</div>
<div class="btn" style="left:145px;top:1111px;width:171px;height:39px;border-width:1.5px">Learn More <svg viewBox="0 0 30 10"><path d="M0 5h27M23 1l4 4-4 4" stroke="currentColor" stroke-width="1.5" fill="none"/></svg></div>
<div class="photo" style="left:709px;top:788px;width:359px;height:362px;background:linear-gradient(160deg,#c9a46b 0%,#9fa4a7 45%,#6f7a55 75%,#8c8f92 100%)" role="img" aria-label="Two builders in hard hats reviewing plans under a timber roof frame"></div>

<!-- SERVICES -->
<div class="abs kicker" style="top:1236px">What We Do</div>
<div class="abs sec-title head" style="top:1262px"><span class="accent">Our</span> Services</div>

<div class="card active" style="left:165px">
  <svg class="icon" viewBox="0 0 70 76" fill="none" stroke="var(--red)" stroke-width="2"><path d="M2 74h66M8 74V36h20v38M28 74V14l22-10v70M50 74V26h14v48"/><path d="M14 44h8M14 52h8M14 60h8M34 22h10M34 30h10M34 38h10M34 46h10M34 54h10M34 62h10M55 34h5M55 42h5M55 50h5M55 58h5"/></svg>
  <h3>Architecture &amp;<br>Building</h3>
  <p>Lorem Ipsum has been the industry's standard &nbsp;text ever since the, when an unknown been industry</p>
  <div class="btn solid">Learn More <svg viewBox="0 0 30 10"><path d="M0 5h27M23 1l4 4-4 4" stroke="currentColor" stroke-width="1.5" fill="none"/></svg></div>
</div>
<div class="card" style="left:465px">
  <svg class="icon" viewBox="0 0 70 76" fill="none" stroke="var(--red)" stroke-width="2"><path d="M22 22a13 13 0 0 1 26 0zM19 22h32M35 6v5"/><circle cx="35" cy="32" r="9"/><path d="M14 74V58a10 10 0 0 1 10-10h22a10 10 0 0 1 10 10v16"/><rect x="6" y="56" width="58" height="10" rx="5"/></svg>
  <h3>Construction<br>Consultants</h3>
  <p>Lorem Ipsum has been the industry's standard &nbsp;text ever since the, when an unknown been industry</p>
  <div class="btn">Learn More <svg viewBox="0 0 30 10"><path d="M0 5h27M23 1l4 4-4 4" stroke="currentColor" stroke-width="1.5" fill="none"/></svg></div>
</div>
<div class="card" style="left:763px">
  <svg class="icon" viewBox="0 0 70 76" fill="none" stroke="var(--red)" stroke-width="2"><path d="M6 74V8h18v66M24 74V30h22v44M2 74h44"/><path d="M10 16h10M10 26h10M10 36h10M10 46h10M28 38h6M28 48h6M28 58h6M38 38h4M38 48h4"/><circle cx="56" cy="40" r="7"/><path d="M56 26v6M56 48v6M42 40h6M64 40h6M46 30l4 4M62 46l4 4M66 30l-4 4M50 46l-4 4"/></svg>
  <h3>Construction<br>Management</h3>
  <p>Lorem Ipsum has been the industry's standard &nbsp;text ever since the, when an unknown been industry</p>
  <div class="btn">Learn More <svg viewBox="0 0 30 10"><path d="M0 5h27M23 1l4 4-4 4" stroke="currentColor" stroke-width="1.5" fill="none"/></svg></div>
</div>

<!-- PROJECTS -->
<svg class="abs" style="left:0;top:1820px" width="1200" height="780">
  <path d="M166 6L252 76H201V224H166Z" fill="var(--red)"/>
  <path d="M971 415V685H875" stroke="var(--orange)" stroke-width="2" fill="none"/>
  <g fill="#222">
    <circle cx="1005" cy="100" r="1.6"/><circle cx="1020" cy="100" r="1.6"/><circle cx="1035" cy="100" r="1.6"/>
    <circle cx="1020" cy="115" r="1.6"/><circle cx="1035" cy="115" r="1.6"/><circle cx="1020" cy="130" r="1.6"/><circle cx="1035" cy="130" r="1.6"/>
    <circle cx="1020" cy="145" r="1.6"/><circle cx="1035" cy="145" r="1.6"/><circle cx="1020" cy="160" r="1.6"/><circle cx="1035" cy="160" r="1.6"/>
    <circle cx="1020" cy="175" r="1.6"/><circle cx="1035" cy="175" r="1.6"/><circle cx="1020" cy="190" r="1.6"/><circle cx="1035" cy="190" r="1.6"/>
    <circle cx="1020" cy="205" r="1.6"/><circle cx="1035" cy="205" r="1.6"/><circle cx="1035" cy="220" r="1.6"/><circle cx="1035" cy="235" r="1.6"/>
    <circle cx="618" cy="140" r="1.6"/><circle cx="618" cy="155" r="1.6"/><circle cx="618" cy="170" r="1.6"/><circle cx="618" cy="185" r="1.6"/><circle cx="618" cy="200" r="1.6"/><circle cx="618" cy="215" r="1.6"/><circle cx="618" cy="230" r="1.6"/><circle cx="618" cy="245" r="1.6"/><circle cx="618" cy="260" r="1.6"/><circle cx="618" cy="275" r="1.6"/>
    <circle cx="182" cy="377" r="1.6"/><circle cx="197" cy="377" r="1.6"/><circle cx="182" cy="392" r="1.6"/><circle cx="197" cy="392" r="1.6"/><circle cx="182" cy="407" r="1.6"/><circle cx="197" cy="407" r="1.6"/><circle cx="182" cy="422" r="1.6"/><circle cx="197" cy="422" r="1.6"/><circle cx="182" cy="437" r="1.6"/><circle cx="197" cy="437" r="1.6"/><circle cx="182" cy="452" r="1.6"/><circle cx="197" cy="452" r="1.6"/>
  </g>
</svg>
<div class="abs sec-title head" style="left:285px;top:1826px;width:auto;text-align:left"><span class="accent">Our</span> Projects</div>
<div class="photo" style="left:201px;top:1894px;width:400px;height:390px;background:linear-gradient(180deg,#c9d3da 0%,#5a5e63 40%,#3a3c40 80%,#8d8e8f 100%)" role="img" aria-label="Modern dark-clad apartment building with open balconies"></div>
<div class="abs" style="left:201px;top:2202px;width:181px;height:82px;background:rgba(235,61,31,.92);padding:16px 0 0 26px;font-family:'Lexend',sans-serif;font-weight:600;font-size:16px;line-height:23px;color:var(--white);text-transform:uppercase">Architecture<br>&amp; Building</div>
<div class="photo" style="left:623px;top:1943px;width:389px;height:292px;background:linear-gradient(180deg,#4a3d33 0%,#1e1f22 30%,#7a7b7d 65%,#9a9b9d 100%)" role="img" aria-label="Office reception with concrete counter, pendant lights and yellow accent wall"></div>
<div class="photo" style="left:412px;top:2311px;width:463px;height:262px;background:linear-gradient(180deg,#e8e8e6 0%,#cfc8bd 45%,#a98a65 70%,#777 100%)" role="img" aria-label="Office kitchenette with wooden cabinets, fridge and white chairs"></div>

<!-- NEWS -->
<div class="abs kicker" style="top:2653px">Stay Updated</div>
<div class="abs sec-title head" style="top:2679px"><span class="accent">Latest</span> News</div>

<div class="news" style="left:102px">
  <div class="frame"></div>
  <div class="photo" style="left:0;top:0;width:284px;height:241px;background:linear-gradient(180deg,#c8d8e8 0%,#e8ecef 50%,#f2f2f2 75%,#8f9295 100%)" role="img" aria-label="Curved white futuristic building against a pale sky"></div>
  <div class="date">14 April 2022</div>
  <h4>Lorem Ipsum Industry's !</h4>
  <p>Lorem Ipsum has been the industry standard dummy text ever since the, when unknown printer took a galley &nbsp;type scrambled</p>
  <span class="more" style="left:252px">More</span>
</div>
<div class="news" style="left:470px">
  <div class="frame"></div>
  <div class="photo" style="left:0;top:0;width:283px;height:241px;background:linear-gradient(160deg,#d89a66 0%,#b5723f 40%,#8d5a33 70%,#c5a084 100%)" role="img" aria-label="Timber house framing under construction"></div>
  <div class="date">14 April 2022</div>
  <h4>Lorem Ipsum Industry's !</h4>
  <p>Lorem Ipsum has been the industry standard dummy text ever since the, when unknown printer took a galley &nbsp;type scrambled</p>
  <span class="more" style="left:252px">More</span>
</div>
<div class="news" style="left:827px">
  <div class="frame" style="left:255px"></div>
  <div class="photo" style="left:0;top:0;width:285px;height:241px;background:linear-gradient(180deg,#f0efec 0%,#e0ddd8 50%,#9a7b5e 75%,#5d6b72 100%)" role="img" aria-label="Bright dining room with wooden table and teal chairs"></div>
  <div class="date">14 April 2022</div>
  <h4>Lorem Ipsum Industry's !</h4>
  <p>Lorem Ipsum has been the industry standard dummy text ever since the, when unknown printer took a galley &nbsp;type scrambled</p>
  <span class="more" style="left:254px">More</span>
</div>

<!-- CONTACT -->
<svg class="abs" style="left:0;top:3200px" width="1200" height="680">
  <path d="M771 17L1007 249H918" stroke="var(--orange)" stroke-width="2" fill="none"/>
  <path d="M252 541H536V648H252Z" fill="var(--red)"/>
  <g fill="#222">
    <circle cx="214" cy="512" r="1.6"/><circle cx="229" cy="512" r="1.6"/><circle cx="244" cy="512" r="1.6"/><circle cx="259" cy="512" r="1.6"/>
    <circle cx="214" cy="527" r="1.6"/><circle cx="229" cy="527" r="1.6"/><circle cx="244" cy="527" r="1.6"/><circle cx="259" cy="527" r="1.6"/>
    <circle cx="214" cy="542" r="1.6"/><circle cx="229" cy="542" r="1.6"/><circle cx="244" cy="542" r="1.6"/>
    <circle cx="214" cy="557" r="1.6"/><circle cx="229" cy="557" r="1.6"/><circle cx="244" cy="557" r="1.6"/>
    <circle cx="214" cy="572" r="1.6"/><circle cx="229" cy="572" r="1.6"/><circle cx="244" cy="572" r="1.6"/>
    <circle cx="214" cy="587" r="1.6"/><circle cx="229" cy="587" r="1.6"/><circle cx="244" cy="587" r="1.6"/>
  </g>
</svg>
<div class="abs contact-card"></div>
<div class="abs sec-title head" style="top:3368px"><span class="accent">Contact</span> Us</div>
<div class="abs kicker" style="top:3413px;font-size:12.5px;color:#666">If you have any Question for contact us today !</div>
<div class="field" style="left:367px;top:3464px;width:465px;height:41px">Name *</div>
<div class="field" style="left:367px;top:3518px;width:465px;height:42px">Email *</div>
<div class="field" style="left:367px;top:3573px;width:225px;height:40px">Phone*</div>
<div class="field" style="left:607px;top:3573px;width:225px;height:40px">Services*
  <svg class="abs" style="right:12px;top:16px" width="9" height="7" viewBox="0 0 9 7"><path d="M0 0H9L4.5 7Z" fill="var(--red)"/></svg></div>
<div class="field" style="left:367px;top:3622px;width:465px;height:91px">Message *</div>
<div class="btn" style="left:527px;top:3725px;width:119px;height:39px;border-width:1.5px;font-size:14px">Submit <svg viewBox="0 0 30 10"><path d="M0 5h27M23 1l4 4-4 4" stroke="currentColor" stroke-width="1.5" fill="none"/></svg></div>

<!-- FOOTER -->
<div class="abs footer">
  <div class="abs" style="left:59px;top:60px;display:flex;align-items:center;gap:12px">
    <span class="logo-mark" style="width:24px;height:24px"></span>
    <span style="font-family:'Lexend',sans-serif;font-weight:700;font-size:21px;line-height:1.05;color:var(--white);text-transform:uppercase">Oak Harbor<br>Construction</span>
  </div>
  <div class="abs small" style="left:62px;top:132px;font-style:italic">We Specialize In Commercial And Residential Remodels, As<br>Well As Ground-Up Construction</div>

  <div class="fh" style="left:488px;top:56px"><span class="accent">Contact</span> Us</div>
  <svg class="abs" style="left:488px;top:97px" width="18" height="22" viewBox="0 0 18 22" fill="none" stroke="var(--red)" stroke-width="1.5"><path d="M9 21s7-7 7-12A7 7 0 0 0 2 9c0 5 7 12 7 12z"/><circle cx="9" cy="9" r="2.5"/></svg>
  <div class="abs small" style="left:527px;top:96px"><span style="color:var(--red)">OAK HARBOR CONSTRUCTION</span><br>101 - Lorem ipsum simple text print<br>type setting text industry !</div>
  <svg class="abs" style="left:488px;top:168px" width="18" height="18" viewBox="0 0 24 24" fill="none" stroke="var(--red)" stroke-width="1.8"><path d="M5 3h4l2 5-3 2a11 11 0 0 0 6 6l2-3 5 2v4a2 2 0 0 1-2 2A17 17 0 0 1 3 5a2 2 0 0 1 2-2z"/></svg>
  <div class="abs" style="left:527px;top:167px;font-size:13px;color:var(--white)">1.480.555.0142</div>
  <svg class="abs" style="left:488px;top:205px" width="19" height="14" viewBox="0 0 19 14" fill="none" stroke="var(--red)" stroke-width="1.5"><rect x=".75" y=".75" width="17.5" height="12.5"/><path d="M1 1l8.5 7L18 1"/></svg>
  <div class="abs small" style="left:527px;top:202px">info@oakharborbuild.com</div>

  <div class="fh" style="left:870px;top:56px"><span class="accent">Site</span> Map</div>
  <ul class="abs sitemap small" style="left:870px;top:96px">
    <li style="top:0">About</li>
    <li style="top:24px">Services</li>
    <li style="top:48px">Projects</li>
    <li style="top:72px">News</li>
    <li style="top:96px">Contact</li>
  </ul>

  <div class="abs" style="left:0;top:268px;width:1200px;height:1px;background:#2a2a2a"></div>
  <div class="abs" style="left:0;top:290px;width:1200px;text-align:center;font-size:11px">©OAK HARBOR CONSTUCTION - 2022 All rights reserved.</div>
</div>
<div class="social" style="left:59px"></div>
<div class="social" style="left:107px"></div>
<div class="social" style="left:156px"></div>

</body>
</html>
```